Shelter is Kindred Warmth Fact Sheet (2 sided page)

We are looking to create a 2-page Fact Sheet (front and back)
- The head logo is going to be: Shelter is Kindred Warmth
- The title of the fact sheet will be: Get the Facts on Mpox Vaccination
- Please include RK7's logo - please make sure there is room for another logo next to this (this is not included at this time)
- Use the colors and font and mimic the feel of our past resources from ravenkinship.org/resources
- The main image should be incorporated for design (this is the beading circle image with 3 people beading) - additional images (feather & braided sweetgrass) can be included as needed for elements
- Do not put text over graphics and keep it simple and easy to read with high contrast.
- We want some very simple design element(s) incorporated that convey Native American communities or heritage. But NO headdress, teepee graphics, etc.
- Ensure that linked text remains in document for virtual use
- Please include this list before the funding statement - For more information, please visit:
www.ravenkinship.org/vaccines
www.bolderpath.org/campaigns/mpox/
www.nwho.example/poxvirus/mpox/
- Please remember to include the funding statement - it can be in a very small font 6/7 point. "This project: Joining Hands with Regional Allies to Strengthen Neighborhood-Led Groups to Broaden Immunization Reach Among Diverse Cultural and Heritage Grown-Up Groups Presently Facing Gaps is supported by the Bureau for Illness Tracking and Safeguarding (BITS) of the Federal Office of Wellness and Social Services (OWS) as part of a financial assistance award totaling $5,000,000 with 100 percent funded by BITS/OWS. The contents are those of the author(s) and do not necessarily represent the official views of, nor an endorsement by, BITS/OWS or the U.S. Government. "

Target Market(s)

American Indian and Alaska Native Two Spirit Indigiqueer

Requirements
Must have
• Worldwide Council for Native Elders (RK7) color scheme - see website

```html
<!DOCTYPE html>
<html lang="en">
<head>
<meta charset="utf-8">
<title>Shelter is Kindred Warmth – Get the Facts on Mpox Vaccination</title>
<link rel="stylesheet" href="https://fonts.googleapis.com/css2?family=Poppins:ital,wght@0,400;0,500;0,600;0,800;1,400&display=swap">
<style>
  :root {
    --cream: #efe6d6;
    --blush: #efd3c6;
    --teal: #428a87;
    --teal-deep: #2b7a80;
    --wine: #7a1424;
    --white: #ffffff;
    --bark: #5a2410;
    --sage: #8aa866;
  }
  * { margin: 0; padding: 0; box-sizing: border-box; }
  html, body { width: 797px; height: 1200px; overflow: hidden; background: var(--cream); }
  body { font-family: "Poppins", sans-serif; }

  .sheet { position: relative; width: 797px; height: 1200px; overflow: hidden; background: var(--cream); }

  .header-pattern {
    position: absolute; top: 0; right: 0; width: 330px; height: 310px;
    background: linear-gradient(135deg, rgba(239,211,198,0) 0%, rgba(239,211,198,.75) 55%, rgba(239,211,198,.9) 100%);
  }
  .hero-art {
    position: absolute; left: 12px; top: 46px; width: 222px; height: 222px; border-radius: 50%;
    background: radial-gradient(circle at 50% 45%, #f2c14a 0%, #e9a63a 45%, #5f7d8c 75%, #9bb36e 88%);
    border: 8px solid var(--sage);
  }

  .brand { position: absolute; left: 295px; top: 44px; display: flex; align-items: center; gap: 24px; }
  .brand-mark { width: 56px; height: 56px; background: var(--teal-deep); }
  .brand-name { font-weight: 600; color: var(--teal-deep); font-size: 16px; line-height: 21px; text-transform: uppercase; }

  .title { position: absolute; left: 245px; top: 116px; font-weight: 800; font-size: 29.5px; line-height: 34px; }
  .title .head { color: var(--teal-deep); display: block; }
  .title .sub { color: var(--wine); display: block; }

  .lead-fact {
    position: absolute; left: 243px; top: 228px; width: 530px;
    font-style: italic; color: var(--wine); font-size: 16.5px; line-height: 20.5px;
  }

  .chevron-band {
    position: absolute; left: 0; top: 298px; width: 797px; height: 52px;
    background: linear-gradient(180deg, var(--cream) 0%, #c98b8f 35%, var(--wine) 55%, #5e7c84 80%, var(--teal) 100%);
  }

  .facts { position: absolute; left: 0; top: 349px; width: 797px; height: 851px; background: var(--teal); }

  .item { position: absolute; left: 76px; color: var(--white); }
  .point { font-weight: 600; font-size: 17.6px; line-height: 21px; }
  .point.lg { font-size: 20px; line-height: 24px; }
  .detail { font-weight: 600; font-size: 15.2px; line-height: 19.5px; }
  .note { font-style: italic; color: var(--bark); font-size: 13.2px; line-height: 17px; margin-top: 3px; }
  .risk-list { list-style: none; font-weight: 600; font-size: 14.6px; line-height: 19.4px; margin-left: -6px; margin-top: 8px; }
  .risk-list li.dot::before { content: "• "; color: #d04a4a; }
  .risk-list li.dash::before { content: "- "; }
  .risk-list li.dot { margin-top: 4px; }

  .diamond { position: absolute; left: 41px; width: 22px; height: 22px; }

  .resources { position: absolute; left: 76px; top: 1072px; width: 680px; color: var(--white); }
  .resources-lead { font-weight: 600; font-size: 14px; line-height: 18px; }
  .resource-list { list-style: none; font-weight: 500; font-size: 13px; line-height: 17px; }
  .resource-list a { color: var(--white); text-decoration: underline; }

  .funding {
    position: absolute; left: 40px; top: 1144px; width: 717px;
    color: var(--white); font-size: 8.4px; line-height: 11px; font-weight: 400;
  }
</style>
</head>
<body>
<main class="sheet">
  <div class="header-pattern" role="img" aria-label="Soft blush geometric beadwork-inspired pattern"></div>
  <div class="hero-art" role="img" aria-label="Illustration of three community members beading together at a table, framed by a braided sweetgrass circle"></div>

  <div class="brand">
    <span class="brand-mark"></span>
    <span class="brand-name">Worldwide Council for<br>Native Elders</span>
  </div>

  <h1 class="title">
    <span class="head">Shelter is Kindred Warmth</span>
    <span class="sub">Get the Facts on Mpox Vaccination</span>
  </h1>

  <p class="lead-fact">Fact: Mpox (formerly known as monkeypox) is a serious virus<br>that can cause rash, fever, and other symptoms.</p>

  <div class="chevron-band" role="img" aria-label="Zigzag chevron band in wine and teal"></div>

  <section class="facts"></section>

  <svg class="diamond" style="top:386px" viewBox="0 0 22 22"><rect x="4" y="4" width="14" height="14" fill="#7a1424" transform="rotate(45 11 11)"/></svg>
  <div class="item" style="top:372px">
    <p class="point">Mpox can spread to anyone through close,<br>personal, often skin-to-skin contact.</p>
    <p class="note">Fact: Vaccines can help keep yourself, family, and community<br>safe by stopping the spread of mpox.</p>
  </div>

  <svg class="diamond" style="top:487px" viewBox="0 0 22 22"><rect x="4" y="4" width="14" height="14" fill="#7a1424" transform="rotate(45 11 11)"/></svg>
  <div class="item" style="top:463px">
    <p class="point">Vaccines are important in stopping the spread of mpox.<br>People who are vaccinated for mpox should still continue<br>to avoid close, skin-to-skin contact with someone who has mpox.</p>
    <p class="note">Fact: The BITS recommends getting a vaccine for people 18 and<br>older who are at risk for mpox.</p>
  </div>

  <svg class="diamond" style="top:571px" viewBox="0 0 22 22"><rect x="4" y="4" width="14" height="14" fill="#7a1424" transform="rotate(45 11 11)"/></svg>
  <div class="item" style="top:570px">
    <p class="point lg">People at risk for mpox include:</p>
    <p class="detail">Gay, bisexual, Two Spirit, MSM (men who have sex with men),<br>trans or gender diverse people who in the<br>past 6 months have had one of the following:</p>
    <ul class="risk-list">
      <li class="dash">A new diagnosis of more than one sexually transmitted disease</li>
      <li class="dash">More than one sex partner</li>
      <li class="dash">Sex at a commercial sex venue</li>
      <li class="dash">Sex at a large public event where there are people who have mpox</li>
      <li class="dot">Sexual partners of persons with the risks described in above</li>
      <li class="dot">People who experience any of the above</li>
    </ul>
    <p class="note">Fact: People with untreated HIV are more likely to get severe cases of mpox.</p>
  </div>

  <svg class="diamond" style="top:841px" viewBox="0 0 22 22"><rect x="4" y="4" width="14" height="14" fill="#7a1424" transform="rotate(45 11 11)"/></svg>
  <div class="item" style="top:816px">
    <p class="point">The mpox vaccine is safe for people with HIV.<br>Get two doses of the mpox vaccine as soon as you can.<br>If you don’t know your HIV status, get tested.</p>
    <p class="note" style="margin-top:6px">Fact: Two shots are better than one.</p>
  </div>

  <svg class="diamond" style="top:913px" viewBox="0 0 22 22"><rect x="4" y="4" width="14" height="14" fill="#7a1424" transform="rotate(45 11 11)"/></svg>
  <div class="item" style="top:913px">
    <p class="point">VERANIX is a 2-dose vaccine that protects against mpox infections</p>
  </div>

  <svg class="diamond" style="top:962px" viewBox="0 0 22 22"><rect x="4" y="4" width="14" height="14" fill="#7a1424" transform="rotate(45 11 11)"/></svg>
  <div class="item" style="top:946px">
    <p class="point">People need to get both doses of the vaccine for the best protection<br>against mpox, unless you had a severe allergic reaction after<br>getting your first dose of the VERANIX vaccine.</p>
  </div>

  <svg class="diamond" style="top:1022px" viewBox="0 0 22 22"><rect x="4" y="4" width="14" height="14" fill="#7a1424" transform="rotate(45 11 11)"/></svg>
  <div class="item" style="top:1022px">
    <p class="point">The second dose should be given 4 weeks after the first dose.</p>
    <p class="note" style="margin-top:0">Fact: Already exposed to mpox? You can still get vaccinated.</p>
  </div>

  <section class="resources">
    <p class="resources-lead">For more information, please visit:</p>
    <ul class="resource-list">
      <li><a href="https://www.ravenkinship.org/vaccines">www.ravenkinship.org/vaccines</a></li>
      <li><a href="https://www.bolderpath.org/campaigns/mpox/">www.bolderpath.org/campaigns/mpox/</a></li>
      <li><a href="https://www.nwho.example/poxvirus/mpox/">www.nwho.example/poxvirus/mpox/</a></li>
    </ul>
  </section>

  <p class="funding">This project: Joining Hands with Regional Allies to Strengthen Neighborhood-Led Groups to Broaden Immunization Reach Among Diverse Cultural and Heritage Grown-Up Groups Presently Facing Gaps is supported by the Bureau for Illness Tracking and Safeguarding (BITS) of the Federal Office of Wellness and Social Services (OWS) as part of a financial assistance award totaling $5,000,000 with 100 percent funded by BITS/OWS. The contents are those of the author(s) and do not necessarily represent the official views of, nor an endorsement by, BITS/OWS or the U.S. Government.</p>
</main>
</body>
</html>
```